Business Card Design for Law firm - already have logo

Now that we have a logo, we need a business card design - our logo is attached -it is salaryman font if that helps - we would like a file that can be uploaded to cardquill (www.cardquill-example.com) using the logo and with the following information on it:
Quenby Law Firm, P.C.
Delwyn Quenby, Esq.
5817 SW 19th Ave.
Fernhollow, OR 97990
971.555.0142 phone
971.555.0187 fax
del@quenby-example.net
Chatwave: delquenby
Talkline: delwyn.quenby@mailbox-example.com
Target Market(s)
our business cards are distributed to corporate executives, technology professionals and healthcare providers
Industry/Entity Type
Business
Look and feel

```html
<!DOCTYPE html>
<html lang="en">
<head>
<meta charset="utf-8">
<title>Quenby Law Firm, P.C. – Business Card</title>
<link rel="stylesheet" href="https://fonts.googleapis.com/css2?family=Arimo:wght@400&display=swap">
<style>
  :root {
    --card-bg: #ffffff;
    --ink: #000000;
    --accent-red: #e0201c;
  }
  * { margin: 0; padding: 0; box-sizing: border-box; }
  html, body {
    width: 1200px;
    height: 688px;
    overflow: hidden;
    background: var(--card-bg);
  }
  .business-card {
    position: relative;
    width: 1200px;
    height: 688px;
    background: var(--card-bg);
    font-family: "Arimo", Arial, sans-serif;
    color: var(--ink);
  }
  .brand-mark {
    position: absolute;
    left: 47px;
    top: 28px;
    width: 150px;
    height: 150px;
    background: var(--ink);
  }
  .firm-name {
    position: absolute;
    left: 47px;
    top: 224px;
    font-size: 38px;
    font-weight: 400;
    letter-spacing: 6px;
    text-transform: uppercase;
    color: var(--ink);
    line-height: 1;
    white-space: nowrap;
  }
  .contact-details {
    position: absolute;
    left: 49px;
    top: 388px;
    list-style: none;
    font-size: 30px;
    line-height: 39px;
    color: var(--ink);
    white-space: nowrap;
  }
  .attorney-name {
    position: absolute;
    left: 736px;
    top: 386px;
    font-size: 43px;
    font-weight: 400;
    color: var(--accent-red);
    line-height: 1;
    white-space: nowrap;
  }
</style>
</head>
<body>
  <main class="business-card">
    <div class="brand-mark" aria-hidden="true"></div>
    <h1 class="firm-name">Quenby Law Firm, P.C.</h1>

    <ul class="contact-details">
      <li class="address-line">5817 SW 19th Ave.</li>
      <li class="address-line">Fernhollow, OR 97990</li>
      <li class="phone">971.555.0142 phone</li>
      <li class="fax">971.555.0187 fax</li>
      <li class="email">del@quenby-example.net</li>
      <li class="messenger">Chatwave: delquenby</li>
      <li class="chat">Talkline: delwyn.quenby@mailbox-example.com</li>
    </ul>

    <p class="attorney-name">Delwyn Quenby, Esq.</p>
  </main>
</body>
</html>
```